Home and Garden business needs a Facebook Design

We need a design for a Home and Garden business called Meadow and Hearth. Our main focus is on perennial plants and home décor. We want to project an image that's a combination of Clara Dunmores Keeping and Finer Rooms and Orchards. The main focus should be on perennial plants and gardening with a secondary emphasis on home décor. Our target customers are homeowners between the age of 30 and 65 with a strong passion for gardening and 'Do it Yourselfers'. Our logo is green and we would like to see any color combinations that go with the logo. The final design should communicate the joy and pride of improving your home and gardens.
Target Market(s)
Homeowners 30 - 65
Industry/Entity Type
Home And Garden
Requirements
Must have
- for an idea of what we are after please take a look at https://www.brindlepost.example/TallyBlooms
- https://www.brindlepost.example/claradunmore
- https://www.brindlepost.example/NookFieldHaven

```html
<!DOCTYPE html>
<html lang="en">
<head>
<meta charset="utf-8">
<title>Meadow &amp; Hearth — Page Cover</title>
<link rel="stylesheet" href="https://fonts.googleapis.com/css2?family=Exo+2:wght@400;500;600&family=Libre+Baskerville:wght@700&family=Open+Sans:wght@400;600;700&display=swap">
<style>
  :root {
    --rose-light: #f4c6d8;
    --rose-mid: #e59bbb;
    --rose-deep: #c9709a;
    --quote-band: rgba(168, 48, 98, 0.82);
    --white: #ffffff;
    --ink: #141823;
    --muted: #6d7179;
    --leaf: #5aa83a;
    --frame-line: #c9ccd3;
    --button-face: #f6f7f9;
    --button-line: #a9afbc;
    --button-ink: #4e5665;
    --link-blue: #3b5998;
  }
  * { box-sizing: border-box; margin: 0; padding: 0; }
  html, body { width: 1200px; height: 543px; overflow: hidden; background: var(--white); }
  .page-header { position: relative; width: 1200px; height: 543px; background: var(--white); }
  .cover-photo {
    position: absolute; left: 0; top: 0; width: 1200px; height: 444px;
    background:
      radial-gradient(circle at 20% 30%, var(--rose-light) 0 12%, transparent 30%),
      radial-gradient(circle at 55% 65%, var(--rose-light) 0 10%, transparent 28%),
      radial-gradient(circle at 85% 75%, var(--rose-light) 0 10%, transparent 26%),
      linear-gradient(135deg, var(--rose-mid), var(--rose-deep) 55%, var(--rose-mid));
  }
  .quote-band {
    position: absolute; left: 739px; top: 35px; width: 461px; height: 219px;
    background: var(--quote-band); color: var(--white);
    font-family: "Exo 2", sans-serif; text-align: center;
    display: flex; flex-direction: column; justify-content: center; align-items: center;
    padding-right: 8px;
  }
  .quote-line { font-size: 34px; font-weight: 400; letter-spacing: 1px; line-height: 1.15; }
  .quote-accent { font-size: 66px; font-weight: 600; letter-spacing: 10px; line-height: 1.05; }
  .profile-frame {
    position: absolute; left: 31px; top: 296px; width: 241px; height: 240px;
    background: var(--white); border: 1px solid var(--frame-line);
    box-shadow: 0 1px 3px rgba(0,0,0,0.18); padding: 6px;
  }
  .profile-mark {
    width: 100%; height: 100%; display: flex; flex-direction: column;
    align-items: center; justify-content: center; gap: 14px;
  }
  .profile-dot { width: 70px; height: 70px; border-radius: 50%; background: var(--leaf); }
  .profile-name {
    font-family: "Exo 2", sans-serif; font-weight: 600; font-size: 24px; color: var(--leaf);
  }
  .page-title {
    position: absolute; left: 289px; top: 452px;
    font-family: "Libre Baskerville", serif; font-weight: 700; font-variant: small-caps;
    font-size: 28px; color: var(--ink); letter-spacing: 0.5px;
  }
  .page-stats {
    position: absolute; left: 290px; top: 494px;
    font-family: "Open Sans", sans-serif; font-size: 15px; color: var(--muted);
  }
  .action-button {
    position: absolute; top: 468px; height: 33px;
    background: var(--button-face); border: 1px solid var(--button-line); border-radius: 3px;
    font-family: "Open Sans", sans-serif; font-weight: 700; font-size: 16px; color: var(--button-ink);
    display: flex; align-items: center; justify-content: center; gap: 6px;
  }
  .button-liked { left: 887px; width: 96px; }
  .button-message { left: 998px; width: 98px; border-radius: 3px 0 0 3px; }
  .button-settings { left: 1095px; width: 70px; border-radius: 0 3px 3px 0; }
</style>
</head>
<body>
<main class="page-header">
  <div class="cover-photo" role="img" aria-label="Close-up photograph of a bunch of soft pink roses filling the cover"></div>

  <div class="quote-band">
    <p class="quote-line">To creaate a little</p>
    <p class="quote-accent">Garden</p>
    <p class="quote-line">is the labor of ages</p>
  </div>

  <div class="profile-frame">
    <div class="profile-mark">
      <span class="profile-dot"></span>
      <span class="profile-name">Meadow &amp; Hearth</span>
    </div>
  </div>

  <h1 class="page-title">Meadow &amp; Hearth</h1>
  <p class="page-stats">2,817 likes · 154 talking about this</p>

  <div class="action-button button-liked">
    <svg width="14" height="12" viewBox="0 0 14 12" aria-hidden="true"><path d="M1 6.5 L5 10 L13 1.5" fill="none" stroke="var(--button-ink)" stroke-width="2.4"/></svg>
    Liked
  </div>
  <div class="action-button button-message">Message</div>
  <div class="action-button button-settings">
    <svg width="16" height="16" viewBox="0 0 16 16" aria-hidden="true">
      <circle cx="8" cy="8" r="4.5" fill="none" stroke="var(--button-ink)" stroke-width="3" stroke-dasharray="2.2 1.3"/>
      <circle cx="8" cy="8" r="1.8" fill="var(--button-ink)"/>
    </svg>
    <svg width="12" height="8" viewBox="0 0 12 8" aria-hidden="true"><path d="M1 1 L6 6.5 L11 1 Z" fill="var(--link-blue)"/></svg>
  </div>
</main>
</body>
</html>
```